Kelbra - Wordpress website for hot new GIF booth

We need a responsive website for a new brand we're launching. Scrolling parallax style. We are a event photo company offering the hottest new GIF booths. We want our site to be sleek, sexy, moving.

Here's some sites we like:
https://www.trondavel.com/us/
http://dravelu.com/
http://zen4.brimquartzix.com/

Target Market(s)

advertising agencies, marketing agencies, major brands, corporate planners, millenials

Industry/Entity Type

Events

Number of Pages Required

1 page

Font styles to use
Sans Serif

Colors
33b8a4
86cfc6
ffffff

Requirements
Must have
• I want it very much like this: https://www.trondavel.com/us/
• lots of imagery, movement
• Here's some competitors:
• http://www.lumatrove.com/
• http://getwrenbolt.com/
• http://www.qtrworks.com/gif-photo-booth-rental/
• http://dravelu.com/
Nice to have
• slider at top with different booth designs
Should not have
• no bulky tabs at top

```html
<!DOCTYPE html>
<html lang="en">
<head>
<meta charset="utf-8">
<title>Kelbra — GIF Booths</title>
<link href="https://fonts.googleapis.com/css2?family=Josefin+Sans:ital,wght@0,300;0,400;0,600;0,700;1,300;1,400&display=swap" rel="stylesheet">
<style>
:root{
  --teal:#33b8a4;
  --teal-soft:#86cfc6;
  --white:#ffffff;
  --ink:#333333;
  --body:#555555;
  --footer-bg:#eeeeee;
  --muted:#777777;
}
*{margin:0;padding:0;box-sizing:border-box}
html,body{width:1200px;height:3346px;overflow:hidden}
body{position:relative;background:var(--white);font-family:"Josefin Sans",Arial,sans-serif;color:var(--body)}
.abs{position:absolute}

/* header */
.site-header{left:0;top:0;width:1200px;height:94px;background:var(--white)}
.brand{left:20px;top:28px;display:flex;align-items:center;gap:10px;font-size:36px;font-weight:400;color:var(--ink);letter-spacing:1px}
.brand-mark{width:22px;height:34px;background:var(--ink)}
.main-nav{right:22px;top:31px;display:flex;align-items:center;gap:27px;font-size:12px;letter-spacing:.5px;color:var(--ink);text-transform:uppercase}
.nav-quote{background:var(--teal);color:var(--white);padding:8px 10px 5px}

/* hero */
.hero{left:0;top:94px;width:1200px;height:604px;background:linear-gradient(120deg,#5a2a2e,#3b3335 40%,#4e2f33 70%,#2f2b2c)}
.hero-copy{left:0;top:210px;width:1200px;text-align:center;color:var(--white)}
.hero-line1{font-size:42px;font-weight:300;letter-spacing:3px}
.hero-line2{font-size:62px;font-weight:700;letter-spacing:2px;line-height:1.1;margin-top:2px}
.hero-line3{font-size:46px;font-weight:300;letter-spacing:7px;margin-top:2px}
.hero-line3 em{font-style:italic;letter-spacing:1px;text-transform:none}
.hero-cta{left:475px;top:500px;width:250px;height:44px;background:var(--teal);color:var(--white);font-size:14px;font-weight:600;letter-spacing:1px;display:flex;align-items:center;justify-content:center;padding-top:3px}

/* features */
.feature{width:330px}
.feature h3{font-size:21px;font-weight:300;color:var(--teal);line-height:28px;margin-bottom:14px}
.feature p{font-size:12px;line-height:19px;color:var(--body)}
.booth-visual{left:420px;top:937px;width:360px;height:524px;background:linear-gradient(160deg,#e9e4e2,#c9c6c8 40%,#b84a4f 75%,#9e2f36);border-radius:4px}

/* band */
.bridge-band{left:0;top:1361px;width:1200px;height:345px;background:var(--teal);color:var(--white);text-align:center}
.bridge-band .line1{position:absolute;top:145px;width:100%;font-size:24px;font-weight:300}
.bridge-band .line2{position:absolute;top:178px;width:100%;font-size:24px;font-weight:300}
.bridge-band .line2 b{font-size:33px;font-weight:300}

/* services */
.service h2{font-size:35px;font-weight:300;color:var(--teal);margin-bottom:22px}
.service p{font-size:12.5px;line-height:22px;color:var(--body);width:480px}
.service-photo{width:526px;height:409px}
.photo-classic{background:linear-gradient(135deg,#9fc3dd,#6f9ec4 50%,#2f7f86)}
.photo-gif{background:linear-gradient(135deg,#8fb1c4,#e9dfd4 55%,#d8c3a2)}
.photo-video{background:linear-gradient(180deg,#e7c44a 0%,#d9d4cc 25%,#8b5e4d 70%,#5b3b30)}
.play-icon{left:220px;top:158px}

/* footer */
.site-footer{left:0;top:3190px;width:1200px;height:156px;background:var(--footer-bg)}
.foot-col{top:48px;font-size:12.5px;line-height:20px;color:var(--body)}
.foot-col h4{font-size:13px;font-weight:400;color:var(--teal);margin-bottom:4px}
.social{display:flex;gap:6px;margin-top:2px}
.social span{width:30px;height:30px;border:2px solid #aaaaaa;border-radius:50%;display:block}
.foot-brand{right:74px;top:42px;display:flex;align-items:center;gap:8px;font-size:32px;color:var(--ink)}
.foot-brand .brand-mark{width:18px;height:30px}
.copyright{right:74px;top:99px;font-size:12px;color:var(--body)}
</style>
</head>
<body>

<header class="site-header abs">
  <div class="brand abs"><span class="brand-mark"></span>KELBRA</div>
  <nav class="main-nav abs">
    <span>The Booth</span><span>Photo</span><span>Gif</span><span>Video</span><span>Events</span><span>About</span><span>Event Galleries</span><span>Blog</span><span>Contact</span><span class="nav-quote">Request a Quote</span>
  </nav>
</header>

<section class="hero abs" role="img" aria-label="Grid of party guests posing with props, dimmed under a dark overlay">
  <div class="hero-copy abs">
    <div class="hero-line1">LIFE IS NOT STATIC.</div>
    <div class="hero-line2">YOUR PHOTOS</div>
    <div class="hero-line3">SHOULDN’T <em>be</em> EITHER.</div>
  </div>
  <div class="hero-cta abs">GET MOVING. #GETKELBRA</div>
</section>

<section class="features">
  <div class="feature abs" style="left:74px;top:743px">
    <h3>We Combine<br>Art &amp; Technology to<br>Let People Create &amp; Share Content.</h3>
    <p>Ut wisi enim ad minim veniam, quis nostrud exerci tation ullamcorper suscipit lobortis nisl ut aliquip ex ea commodo consequat.</p>
  </div>
  <div class="feature abs" style="left:435px;top:743px">
    <h3>We Build Custom, Scalable<br>Event-Technology Platforms<br>For Brands.</h3>
    <p>Ut wisi enim ad minim veniam, quis nostrud exerci tation ullamcorper suscipit lobortis nisl ut aliquip ex ea commodo consequat.</p>
  </div>
  <div class="feature abs" style="left:794px;top:743px">
    <h3>We Build Machines<br>That Connect Social People<br>Around Experiences.</h3>
    <p>Ut wisi enim ad minim veniam, quis nostrud exerci tation ullamcorper suscipit lobortis nisl ut aliquip ex ea commodo consequat.</p>
  </div>
  <div class="feature abs" style="left:74px;top:955px">
    <h3>We Let<br>Your Fans Share<br>Your Brand.</h3>
    <p>Ut wisi enim ad minim veniam, quis nostrud exerci tation ullamcorper suscipit lobortis nisl ut aliquip ex ea commodo consequat.</p>
  </div>
  <div class="feature abs" style="left:794px;top:955px">
    <h3>We Build Custom, Scalable<br>Event-Technology Platforms<br>For Brands.</h3>
    <p>Ut wisi enim ad minim veniam, quis nostrud exerci tation ullamcorper suscipit lobortis nisl ut aliquip ex ea commodo consequat.</p>
  </div>
</section>

<section class="bridge-band abs">
  <div class="line1">We Bridge</div>
  <div class="line2">The <b>Divide Between Digital</b> And <b>Experiential Marketing.</b></div>
</section>

<div class="booth-visual abs" role="img" aria-label="Free-standing GIF booth kiosk beside a guest posing with paper glasses and bow-tie props"></div>

<section class="service abs" style="left:74px;top:1848px">
  <h2>The Classic Photobooth</h2>
  <p>Ut wisi enim ad minim veniam, quis nostrud exerci tation ullamcorper suscipit lobortis nisl ut aliquip ex ea commodo consequat. Duis autem vel eum iriure dolor in hendrerit in vulputate velit esse molestie consequat, vel illum dolore eu feugiat nulla facilisis at vero eros et accumsan et iusto odio dignissim qui blandit praesent luptatum zzril delenit augue duis dolore te feugait nulla facilisi. Nam liber tempor cum soluta nobis eleifend option congue nihil imperdiet doming id quod mazim placerat facer possim assum.</p>
</section>
<div class="service-photo photo-classic abs" style="left:600px;top:1769px" role="img" aria-label="Two friends laughing and sharing a toast"></div>

<div class="service-photo photo-gif abs" style="left:74px;top:2244px" role="img" aria-label="Smiling guest posing playfully in a lace top"></div>
<section class="service abs" style="left:651px;top:2323px">
  <h2>The Animated Gif Booth</h2>
  <p>Ut wisi enim ad minim veniam, quis nostrud exerci tation ullamcorper suscipit lobortis nisl ut aliquip ex ea commodo consequat. Duis autem vel eum iriure dolor in hendrerit in vulputate velit esse molestie consequat, vel illum dolore eu feugiat nulla facilisis at vero eros et accumsan et iusto odio dignissim qui blandit praesent luptatum zzril delenit augue duis dolore te feugait nulla facilisi. Nam liber tempor cum soluta nobis eleifend option congue nihil imperdiet doming id quod mazim placerat facer possim assum.</p>
</section>

<section class="service abs" style="left:74px;top:2796px">
  <h2>The Video Booth</h2>
  <p>Ut wisi enim ad minim veniam, quis nostrud exerci tation ullamcorper suscipit lobortis nisl ut aliquip ex ea commodo consequat. Duis autem vel eum iriure dolor in hendrerit in vulputate velit esse molestie consequat, vel illum dolore eu feugiat nulla facilisis at vero eros et accumsan et iusto odio dignissim qui blandit praesent luptatum zzril delenit augue duis dolore te feugait nulla facilisi. Nam liber tempor cum soluta nobis eleifend option congue nihil imperdiet doming id quod mazim placerat facer possim assum.</p>
</section>
<div class="service-photo photo-video abs" style="left:600px;top:2717px" role="img" aria-label="Guest in sunglasses holding a film clapperboard under party bunting">
  <svg class="play-icon abs" width="90" height="90" viewBox="0 0 90 90" aria-hidden="true">
    <circle cx="45" cy="45" r="40" fill="none" stroke="#ffffff" stroke-width="6"/>
    <path d="M36 28 L63 45 L36 62 Z" fill="#ffffff"/>
  </svg>
</div>

<footer class="site-footer abs">
  <div class="foot-col abs" style="left:74px">
    <h4>Contact Us</h4>
    228, Loremipsum dolor,<br>dosis amer- 88 88 88
  </div>
  <div class="foot-col abs" style="left:254px">
    <h4>General Inquiries</h4>
    info@kelbra.com
  </div>
  <div class="foot-col abs" style="left:399px">
    <h4>Call Us</h4>
    (808) 555.0142
  </div>
  <div class="foot-col abs" style="left:524px">
    <h4>Follow Us</h4>
    <div class="social"><span></span><span></span><span></span><span></span></div>
  </div>
  <div class="foot-brand abs"><span class="brand-mark"></span>KELBRA</div>
  <div class="copyright abs">Copyright 2016 Kelbra. All Rights Reserved</div>
</footer>

</body>
</html>
```